Product Sales Website Design - E-commerce - Shopify etc

We have been selling printing equipment for some time now and think that it will be useful to sell the products on the internet, using a simple e-commerce platform, such as shopify etc. There are roughly a few dozen products - so basically, the idea is to have a modern, simple and clean home page. When someone looks at it, they think, this is it - I want to buy here. I am not going to impose any ideas or say how I want it done.

Just so you know, at the moment there are three categories of products. One being printers, scanners and accessories.

I am excited by this whole project and don't want to have good designers backing out because they feel i am imposing restrictions. Feel free to impress me.

Industry/Entity Type

E-Commerce

Requirements
Must have
• integration with an e-commerce platform is a must or show how to integrate, so I can easily introduce further products.

```html
<!DOCTYPE html>
<html lang="en">
<head>
<meta charset="utf-8">
<title>Print Shop Home</title>
<link href="https://fonts.googleapis.com/css2?family=Arimo:wght@400;700&display=swap" rel="stylesheet">
<style>
:root{
  --ink:#2a2a2a;
  --ink-deep:#0e0e0e;
  --band:#c0c0c0;
  --accent:#12bdf2;
  --green:#21c21e;
  --text:#222;
  --muted:#888;
  --line:#dcdcdc;
  --panel:#f4f3f5;
  --bar:#d6d6d6;
  --white:#fff;
  --device:#1d1d1d;
  --device-mid:#6d6d6d;
  --screen-blue:#2f93d6;
}
*{box-sizing:border-box;margin:0;padding:0}
html,body{width:1200px;height:1125px;overflow:hidden;background:var(--white)}
body{font-family:"Arimo",Arial,sans-serif;color:var(--text);position:relative}
.abs{position:absolute}

.site-header{left:0;top:0;width:1200px;height:71px;background:var(--ink)}
.brand{left:295px;top:27px;color:var(--white);font-weight:700;font-size:15px}
.brand span{color:var(--accent)}
.slogan{left:295px;top:48px;color:var(--white);font-size:11px}
.cart-label{left:793px;top:0;width:62px;height:18px;color:#bbb;font-size:6.5px;font-weight:700;line-height:18px;text-align:right;padding-right:6px}
.cart-label b{color:#f4a51c}
.cart-proceed{left:855px;top:0;width:70px;height:18px;background:#6a6a6a;color:#ddd;font-size:6.5px;font-weight:700;line-height:18px;text-align:center}
.cart-go{left:925px;top:0;width:19px;height:18px;background:var(--accent)}
.main-nav{left:650px;top:50px;width:294px;color:var(--white);font-size:6.5px;font-weight:700;text-align:right;white-space:nowrap}

.latest{left:0;top:71px;width:1200px;height:190px;background:var(--band)}
.latest-title{left:295px;top:113px;font-size:10px;color:#333}
.latest-arrows{left:916px;top:113px;display:flex;gap:2px}
.latest-arrows i{width:13px;height:11px;background:#ececec;display:block;position:relative}
.latest-arrows i.on{background:var(--white)}
.thumb-row{left:295px;top:137px;display:flex;gap:4.8px}
.thumb{width:105px;height:76px;background:var(--white);padding:4px}
.product-photo{width:100%;height:100%;background:radial-gradient(ellipse 38% 42% at 50% 50%,var(--device) 0,#3a3a3a 55%,#b9b9b9 80%,var(--white) 100%)}
.product-photo.screen{background:radial-gradient(ellipse 42% 32% at 50% 48%,var(--device) 0,#444 60%,#c4c4c4 82%,var(--white) 100%)}
.product-photo.router{background:radial-gradient(ellipse 28% 40% at 50% 55%,var(--device-mid) 0,#3d3d3d 50%,#c9c9c9 80%,var(--white) 100%)}
.product-photo.cover{background:radial-gradient(ellipse 40% 45% at 50% 50%,var(--screen-blue) 0,#5c5c5c 55%,#cfcfcf 80%,var(--white) 100%)}
.product-photo.box{background:radial-gradient(ellipse 36% 24% at 50% 55%,var(--device) 0,#333 60%,#c4c4c4 82%,var(--white) 100%)}
.product-photo.laptop{background:radial-gradient(ellipse 38% 40% at 52% 50%,#2f6fc0 0,#2c2c2c 55%,#c1c1c1 80%,var(--white) 100%)}
.latest-caption{left:295px;top:233px;width:649px;text-align:center;font-size:13px;color:#333}

.promo{left:0;top:261px;width:1200px;height:63px;background:var(--ink)}
.promo-text{left:295px;top:277px;width:400px;color:var(--white);font-size:10px;font-weight:700;line-height:12px}
.promo-call{left:750px;top:261px;width:194px;height:63px;background:var(--accent);color:var(--white);font-size:13px;font-weight:700;line-height:63px;text-align:center}

.intro{left:295px;top:332px;width:649px;height:62px;border:1px solid var(--line);text-align:center}
.intro p:first-child{font-size:9.5px;margin-top:13px}
.intro p:last-child{font-size:12px;margin-top:6px}

.offer{left:295px;top:402px;width:442px;height:94px;background:var(--panel)}
.offer-title{left:16px;top:17px;color:#aaa;font-size:14px;font-weight:700;line-height:15px}
.offer-text{left:17px;top:59px;width:100px;color:#aaa;font-size:5.5px;line-height:9px}
.offer-photo{width:90px;height:74px}
.offer .product-photo{background:radial-gradient(ellipse 38% 42% at 50% 50%,var(--device) 0,#3a3a3a 55%,#c8c8c8 80%,var(--panel) 100%)}
.offer .product-photo.screen{background:radial-gradient(ellipse 42% 30% at 50% 48%,var(--device) 0,#444 60%,#c8c8c8 82%,var(--panel) 100%)}

.products-title{left:295px;top:521px;font-size:10.5px;color:#333}
.card{width:145px;height:125px;border:1px solid var(--line);background:var(--white);overflow:hidden}
.card-photo{position:absolute;left:22px;top:8px;width:100px;height:84px}
.card-bar{position:absolute;left:0;bottom:0;width:100%;height:24px;background:var(--bar);font-size:7.5px;line-height:24px;padding-left:10px;color:#333}
.card-buy{position:absolute;right:0;bottom:0;width:48px;height:24px;background:var(--accent);clip-path:polygon(0 0,100% 0,100% 100%,12px 100%)}
.card-buy svg{position:absolute;left:18px;top:5px}
.ribbon{position:absolute;left:0;top:0;width:40px;height:28px;clip-path:polygon(0 0,100% 0,0 100%)}
.ribbon span{position:absolute;left:2px;top:7px;transform:rotate(-35deg);color:var(--white);font-size:7px;font-weight:700;white-space:nowrap}

.side-box{left:750px;width:194px;border:1px solid var(--line);padding:14px 15px}
.side-box h3{font-size:10px;font-weight:400;color:#555;padding-bottom:12px;border-bottom:1px solid var(--line)}
.cat-list{list-style:none;margin-top:10px}
.cat-list li{font-size:6.5px;color:#777;height:15.7px}
.tags{margin-top:10px;font-size:7px;color:#999;line-height:18px}
.tags .hot{color:var(--accent);font-size:9.5px}
.news-title{left:750px;top:709px;font-size:7.5px;font-weight:700;color:#222}
.news-text{left:750px;top:724px;font-size:6.5px;color:#222}
.news-input{left:750px;top:740px;width:128px;height:21px;border:1px solid #eee}
.news-send{left:878px;top:740px;width:66px;height:21px;background:var(--accent);color:var(--white);font-size:7.5px;font-weight:700;line-height:21px;text-align:center}
.pay{left:750px;top:774px;width:194px;height:98px;background:#eeedf2}
.pay h3{position:absolute;left:7px;top:14px;font-size:7.5px;font-weight:400;color:#888;letter-spacing:.3px}
.pay-grid{position:absolute;left:7px;top:33px;display:grid;grid-template-columns:repeat(7,22px);gap:11px 5px}
.pay-grid i{display:block;width:22px;height:13px;border-radius:2px}

.site-footer{left:0;top:890px;width:1200px;height:191px;background:var(--ink)}
.foot-col{top:925px;color:var(--white)}
.foot-col h4{font-size:10px;font-weight:400;margin-bottom:14px}
.foot-col li{list-style:none;font-size:6.5px;color:#bbb;height:13px}
.foot-col.tight li{height:10px}
.foot-news{left:750px;top:925px;color:var(--white)}
.foot-news h4{font-size:10px;font-weight:400}
.foot-news p{font-size:6.5px;color:#bbb;margin-top:18px}
.foot-input{left:750px;top:966px;width:148px;height:21px;background:#4a4a4a}
.foot-submit{left:898px;top:966px;width:46px;height:21px;background:var(--accent);color:var(--ink);font-size:7px;font-weight:700;line-height:21px;text-align:center}
.bottom-bar{left:0;top:1081px;width:1200px;height:44px;background:var(--ink-deep)}
.bottom-brand{left:295px;top:1096px;color:var(--white);font-size:16px}
.bottom-links{left:421px;top:1098px;color:var(--white);font-size:6.5px;line-height:10px}
</style>
</head>
<body>

<header class="abs site-header"></header>
<div class="abs brand">YOUR <span>LOGO</span></div>
<div class="abs slogan">Slogan Goes Here</div>
<div class="abs cart-label">In Your Cart <b>(0)</b></div>
<div class="abs cart-proceed">Proceed</div>
<div class="abs cart-go"><svg width="19" height="18" viewBox="0 0 19 18"><path d="M7 4l5 5-5 5" fill="none" stroke="#fff" stroke-width="2.2"/></svg></div>
<nav class="abs main-nav">Lorem ipsum &nbsp;| &nbsp;Lorem ipsum &nbsp;| &nbsp;Lorem ipsum &nbsp;| &nbsp;Lorem ipsum &nbsp;| &nbsp;Lorem ipsum &nbsp;| &nbsp;Lorem ipsum</nav>

<section class="abs latest"></section>
<div class="abs latest-title">Latest Products</div>
<div class="abs latest-arrows">
  <i><svg width="13" height="11" viewBox="0 0 13 11"><path d="M8 2.5L5 5.5l3 3" fill="none" stroke="#bbb" stroke-width="1.3"/></svg></i>
  <i class="on"><svg width="13" height="11" viewBox="0 0 13 11"><path d="M5 2.5l3 3-3 3" fill="none" stroke="#444" stroke-width="1.3"/></svg></i>
</div>
<div class="abs thumb-row">
  <div class="thumb"><div class="product-photo" role="img" aria-label="Photo of three smartphones"></div></div>
  <div class="thumb"><div class="product-photo router" role="img" aria-label="Photo of a wireless router"></div></div>
  <div class="thumb"><div class="product-photo screen" role="img" aria-label="Photo of a flat screen monitor"></div></div>
  <div class="thumb"><div class="product-photo cover" role="img" aria-label="Illustration of a protection plan"></div></div>
  <div class="thumb"><div class="product-photo box" role="img" aria-label="Photo of a set-top box"></div></div>
  <div class="thumb"><div class="product-photo laptop" role="img" aria-label="Photo of a laptop"></div></div>
</div>
<div class="abs latest-caption">Lorem ipsum dolor sit amet, consectetur adipisicing elit</div>

<section class="abs promo"></section>
<div class="abs promo-text">Lorem ipsum dolor sit amet, consectetur adipisicing elit, sed do eiusmod tempor incididunt ut labore et dolore magna aliqua.</div>
<div class="abs promo-call">Call: 555 014 22907</div>

<section class="abs intro">
  <p>Lorem ipsum dolor sit amet, consectetur adipisicing elit, sed do eiusmod tempor incididunt ut labore et dolore magna aliqua.</p>
  <p>Lorem ipsum dolor sit amet, consectetur adipisicing elit, sed do eiusmod tempor incididunt ut labore et dolore magna</p>
</section>

<section class="abs offer">
  <div class="abs offer-title">SPECIAL<br>OFFER</div>
  <div class="abs offer-text">Lorem ipsum dolor sit amet, con-<br>sectetur adipisicing elit</div>
  <svg class="abs" style="left:130px;top:42px" width="8" height="10" viewBox="0 0 8 10"><path d="M7 0L1 5l6 5z" fill="#bbb"/></svg>
  <div class="abs offer-photo product-photo" role="img" aria-label="Photo of three smartphones" style="left:172px;top:10px"></div>
  <div class="abs offer-photo product-photo screen" role="img" aria-label="Photo of a flat screen monitor" style="left:290px;top:10px"></div>
  <svg class="abs" style="left:380px;top:42px" width="8" height="10" viewBox="0 0 8 10"><path d="M1 0l6 5-6 5z" fill="#bbb"/></svg>
</section>

<div class="abs products-title">PRODUCTS</div>

<article class="abs card" style="left:295px;top:549px">
  <div class="card-photo product-photo" role="img" aria-label="Photo of three smartphones"></div>
  <div class="ribbon" style="background:var(--accent)"><span>New</span></div>
  <div class="card-bar">Product Name</div>
  <div class="card-buy"><svg width="16" height="14" viewBox="0 0 16 14"><path d="M1 1h3l2 8h7l2-6H5" fill="none" stroke="#fff" stroke-width="1.6"/><circle cx="7" cy="12" r="1.3" fill="#fff"/><circle cx="12" cy="12" r="1.3" fill="#fff"/></svg></div>
</article>
<article class="abs card" style="left:444px;top:549px">
  <div class="card-photo product-photo screen" role="img" aria-label="Photo of a flat screen monitor"></div>
  <div class="card-bar">Product Name</div>
  <div class="card-buy"><svg width="16" height="14" viewBox="0 0 16 14"><path d="M1 1h3l2 8h7l2-6H5" fill="none" stroke="#fff" stroke-width="1.6"/><circle cx="7" cy="12" r="1.3" fill="#fff"/><circle cx="12" cy="12" r="1.3" fill="#fff"/></svg></div>
</article>
<article class="abs card" style="left:592px;top:549px">
  <div class="card-photo product-photo" role="img" aria-label="Photo of three smartphones"></div>
  <div class="ribbon" style="background:var(--green)"><span>Off 25%</span></div>
  <div class="card-bar">Product Name</div>
  <div class="card-buy"><svg width="16" height="14" viewBox="0 0 16 14"><path d="M1 1h3l2 8h7l2-6H5" fill="none" stroke="#fff" stroke-width="1.6"/><circle cx="7" cy="12" r="1.3" fill="#fff"/><circle cx="12" cy="12" r="1.3" fill="#fff"/></svg></div>
</article>
<article class="abs card" style="left:295px;top:691px">
  <div class="card-photo product-photo" role="img" aria-label="Photo of three smartphones"></div>
  <div class="card-bar">Product Name</div>
  <div class="card-buy"><svg width="16" height="14" viewBox="0 0 16 14"><path d="M1 1h3l2 8h7l2-6H5" fill="none" stroke="#fff" stroke-width="1.6"/><circle cx="7" cy="12" r="1.3" fill="#fff"/><circle cx="12" cy="12" r="1.3" fill="#fff"/></svg></div>
</article>
<article class="abs card" style="left:444px;top:691px">
  <div class="card-photo product-photo screen" role="img" aria-label="Photo of a flat screen monitor"></div>
  <div class="card-bar">Product Name</div>
  <div class="card-buy"><svg width="16" height="14" viewBox="0 0 16 14"><path d="M1 1h3l2 8h7l2-6H5" fill="none" stroke="#fff" stroke-width="1.6"/><circle cx="7" cy="12" r="1.3" fill="#fff"/><circle cx="12" cy="12" r="1.3" fill="#fff"/></svg></div>
</article>
<article class="abs card" style="left:592px;top:691px">
  <div class="card-photo product-photo" role="img" aria-label="Photo of three smartphones"></div>
  <div class="card-bar">Product Name</div>
  <div class="card-buy"><svg width="16" height="14" viewBox="0 0 16 14"><path d="M1 1h3l2 8h7l2-6H5" fill="none" stroke="#fff" stroke-width="1.6"/><circle cx="7" cy="12" r="1.3" fill="#fff"/><circle cx="12" cy="12" r="1.3" fill="#fff"/></svg></div>
</article>

<aside class="abs side-box" style="top:402px;height:163px">
  <h3>Category</h3>
  <ul class="cat-list">
    <li>Lorem Ipsum &nbsp;&gt;&gt;</li><li>Lorem Ipsum &nbsp;&gt;&gt;</li><li>Lorem Ipsum &nbsp;&gt;&gt;</li>
    <li>Lorem Ipsum &nbsp;&gt;&gt;</li><li>Lorem Ipsum &nbsp;&gt;&gt;</li><li>Lorem Ipsum &nbsp;&gt;&gt;</li>
  </ul>
</aside>
<aside class="abs side-box" style="top:577px;height:113px">
  <h3>Tag Links</h3>
  <p class="tags">resiliation, resiliation, RESILIATION, RESILIER,<br>resilier, résilier, <span class="hot">resiliation abonnement</span>,<br>résiliation abonnement, resiliation mobile</p>
</aside>
<div class="abs news-title">Lorem ipsum dolor sit amet</div>
<div class="abs news-text">Lorem ipsum dolor sit amet, consectetur adipisicing elit</div>
<div class="abs news-input"></div>
<div class="abs news-send">Envoyer</div>
<section class="abs pay">
  <h3>PAYMENT METHOD</h3>
  <div class="pay-grid">
    <i style="background:#3a6fb8"></i><i style="background:#e8e3e0"></i><i style="background:#e6e6ea"></i><i style="background:#2a8fd0"></i><i style="background:#f0c330"></i><i style="background:#8a3ab0"></i><i style="background:#e6e6e6"></i>
    <i style="background:#3a6fb8"></i><i style="background:#e8e3e0"></i><i style="background:#e6e6e6"></i><i style="background:#5a9fd8"></i><i style="background:#222"></i><i style="background:#1a8a4a"></i><i style="background:#d8dce8"></i>
  </div>
</section>

<footer class="abs site-footer"></footer>
<div class="abs foot-col" style="left:295px">
  <h4>Products</h4>
  <ul><li>Lorem ipsum dolor</li><li>Lorem ipsum dolor</li><li>Lorem ipsum dolor</li><li>Lorem ipsum dolor</li><li>Lorem ipsum dolor</li><li>Lorem ipsum dolor</li><li>Lorem ipsum dolor</li></ul>
</div>
<div class="abs foot-col tight" style="left:458px">
  <h4>Site Info</h4>
  <ul><li>Lorem ipsum dolor</li><li>Lorem ipsum dolor</li><li>Lorem ipsum dolor</li></ul>
</div>
<div class="abs foot-col tight" style="left:595px">
  <h4>About Us</h4>
  <ul><li>Lorem ipsum dolor</li><li>Lorem ipsum dolor</li><li>Lorem ipsum dolor</li><li>Lorem ipsum dolor</li><li>Lorem ipsum dolor</li></ul>
</div>
<div class="abs foot-news">
  <h4>Newsletter</h4>
  <p>Lorem ipsum dolor sit amet, consectetur adipisicing elit</p>
</div>
<div class="abs foot-input"></div>
<div class="abs foot-submit">Submit</div>

<div class="abs bottom-bar"></div>
<div class="abs bottom-brand">YOUR LOGO</div>
<div class="abs bottom-links">Home | Terms &amp; Condition | Privacy Policy | Contact Us<br>Copyright All Right Reserved 2014</div>

</body>
</html>
```